BRAVEWELL DISPLAY GROUP Website

Looking for a website design that clearly and powerfully portrays our unique and effective indoor advertising billboards in our network.

Our TinyPlates, TallPlates and GrandFlags are strategically placed in high traffic areas of restaurants, pubs, nightclubs, fitness clubs, colleges and universities, and sports arenas.

Bravewell Display Group is our new name. Our current site is www.plovacorp.ca with our focus now being entirely on our Out-of-Home media. New website address will be www.bravewelldisplay.ca

We need the following sections:

HOME
PRODUCTS (Drop down menu)
-TinyPlates
-TallPlates
-GrandFlags
NETWORKS (Drop down menu)
-Dine-Pour
-Sports
-Campus
EFFECTIVENESS
CAMPAIGNS *This page will show numerous ad campaigns and could be a slide show (see www.plovacorp.ca/KVPL_campaigns.html )
BECOME A PARTNER
CONTACT

Please include social media functions on the homepage such as chirpnet/pagelink/workring

We will be supplying content and photos as required.

Our plan is to have you submit the homepage design to start with, and then we can start judging which styles we like the best and can start narrowing our list. As a second round, we would like to ask the "finalists" to submit a second page (another section of the website) and to see how consistent you are in terms of the look and feel you proposed for the homepage.

Attached is our new logo.

We may require you to upload the final website for us.

Websites that are in similar industry are:
www.torvelix.com
www.quandrafeed.com

Industry/Entity Type

Advertising

Requirements
Must have
• Our network offers advertising solutions that feature: Guaranteed Readership,100% Gender Specific, Frequency, and Captive Audience. Purchasing advertising space in our network are small to medium business owners and advertising agencies booking on behalf of their clients.

Site must be professional and modern looking.
Nice to have
• Moving banner or slide show of some type.

```html
<!DOCTYPE html>
<html lang="en">
<head>
<meta charset="utf-8">
<title>Bravewell Display Group</title>
<link rel="stylesheet" href="https://fonts.googleapis.com/css2?family=Oswald:wght@400;500&family=Noto+Sans:wght@400;700&display=swap">
<style>
:root{
  --blue:#2a66b3;
  --nav-top:#4f8fd8;
  --nav-bottom:#2a64b0;
  --text:#6a6a6a;
  --text-light:#777;
  --grey-mid:#8a8a8a;
  --tick:#8cc63f;
  --rule:#dcdcdc;
  --bg:#ffffff;
}
*{box-sizing:border-box;margin:0;padding:0}
html,body{width:1200px;height:1002px;overflow:hidden;background:var(--bg)}
body{font-family:"Noto Sans",sans-serif;color:var(--text)}
.page{position:relative;width:1200px;height:1002px}
.abs{position:absolute}

.header-art{left:172px;top:18px;width:496px;height:229px;
  background:linear-gradient(180deg,#f2f2f2 0%,#d2d2d2 55%,#9a9a9a 100%)}
.header-art-city{left:668px;top:147px;width:307px;height:100px;
  background:linear-gradient(180deg,#e6e6e6 0%,#c4c4c4 100%)}
.brand{left:172px;top:76px;width:496px;text-align:center;
  font-family:"Noto Sans",sans-serif;font-weight:700;font-size:30px;
  color:var(--blue);letter-spacing:1px;line-height:1.2}

.follow{left:797px;top:84px;display:flex;align-items:center;gap:10px;height:30px}
.follow-label{font-family:"Oswald",sans-serif;font-size:13px;color:var(--grey-mid);text-transform:uppercase}
.social{display:flex;align-items:center;gap:4px;font-size:11px;color:var(--blue);text-decoration:none}
.social-dot{width:12px;height:12px;border-radius:50%;background:var(--blue)}

.main-nav{left:173px;top:247px;width:854px;height:48px;border-radius:8px;
  background:linear-gradient(180deg,var(--nav-top),var(--nav-bottom));
  display:flex;justify-content:space-between;align-items:center;padding:0 40px;
  box-shadow:0 2px 3px rgba(0,0,0,.25)}
.main-nav a{font-family:"Oswald",sans-serif;font-size:17px;color:#fff;text-decoration:none;text-transform:uppercase}

.intro-title{left:173px;top:316px;font-family:"Oswald",sans-serif;font-weight:400;font-size:21px;color:var(--blue);letter-spacing:-.3px}
.features{left:180px;top:356px;list-style:none}
.features li{display:flex;align-items:center;gap:9px;height:31px;font-size:16px;color:var(--text)}
.intro-text{left:173px;top:493px;width:420px;font-size:13.5px;line-height:21px;color:var(--text)}
.hero-photo{left:607px;top:312px;width:420px;height:243px;border-radius:8px;
  background:linear-gradient(160deg,#d9c2ae 0%,#c9a88e 45%,#5aa8d6 100%)}

.product{width:268px}
.product h2{font-family:"Oswald",sans-serif;font-weight:400;font-size:24px;color:var(--blue);text-transform:uppercase;line-height:1;height:30px}
.product-photo{margin-top:8px;width:267px;height:140px}
.product p{margin-top:13px;font-size:12px;line-height:16px;color:var(--text-light);height:64px}
.product .more{display:block;text-align:right;margin-top:17px;font-size:12.5px;color:var(--blue);text-decoration:none}
.p1{left:172px;top:598px}
.p2{left:466px;top:598px}
.p3{left:759px;top:598px}
.p1 .product-photo{background:linear-gradient(90deg,#d9d6cf,#c3c0b8 50%,#e3e1dc)}
.p2 .product-photo{background:linear-gradient(90deg,#3d3a36,#6b6660 50%,#3a3a3a)}
.p3 .product-photo{background:linear-gradient(180deg,#dde3ea 0%,#9fa7b1 50%,#2f7a3a 78%,#b0563c 100%)}

.footer-rule{left:172px;top:918px;width:855px;height:1px;background:var(--rule)}
.footer-info{left:172px;top:932px;font-size:11px;line-height:16px;color:var(--text-light)}
.footer-info strong{font-weight:700}
.footer-nav{right:173px;top:932px;font-size:11px;line-height:16px;color:var(--text-light)}
.footer-nav a{color:var(--blue);text-decoration:none}
.footer-nav span{margin:0 4px}
</style>
</head>
<body>
<div class="page">
  <header>
    <div class="abs header-art" role="img" aria-label="Illustration of an illuminated billboard"></div>
    <div class="abs header-art-city" role="img" aria-label="Illustration of a grey city skyline"></div>
    <div class="abs brand">BRAVEWELL<br>DISPLAY GROUP</div>
    <div class="abs follow">
      <span class="follow-label">Follow us:</span>
      <a class="social" href="#"><span class="social-dot"></span>pagelink</a>
      <a class="social" href="#"><span class="social-dot"></span>chirpnet</a>
      <a class="social" href="#"><span class="social-dot"></span>workring</a>
    </div>
    <nav class="abs main-nav">
      <a href="#">Home</a>
      <a href="#">Products</a>
      <a href="#">Networks</a>
      <a href="#">Effectiveness</a>
      <a href="#">Campaigns</a>
      <a href="#">Become a Partner</a>
      <a href="#">Contact Us</a>
    </nav>
  </header>

  <section>
    <h1 class="abs intro-title">Our network offers advertising solutions that feature:</h1>
    <ul class="abs features">
      <li><svg width="27" height="22" viewBox="0 0 27 22"><path d="M2 12 L9 19 L25 2 L10 14 Z" fill="var(--tick)"/></svg>Guaranteed Readership</li>
      <li><svg width="27" height="22" viewBox="0 0 27 22"><path d="M2 12 L9 19 L25 2 L10 14 Z" fill="var(--tick)"/></svg>100% Gender Specific</li>
      <li><svg width="27" height="22" viewBox="0 0 27 22"><path d="M2 12 L9 19 L25 2 L10 14 Z" fill="var(--tick)"/></svg>Frequency</li>
      <li><svg width="27" height="22" viewBox="0 0 27 22"><path d="M2 12 L9 19 L25 2 L10 14 Z" fill="var(--tick)"/></svg>Captive Audience</li>
    </ul>
    <p class="abs intro-text">Purchasing advertising space in our network are small to medium business owners and advertising agencies booking on behalf of their clients.</p>
    <div class="abs hero-photo" role="img" aria-label="Photo of a group of young people looking upward"></div>
  </section>

  <section>
    <article class="abs product p1">
      <h2>TinyPlates</h2>
      <div class="product-photo" role="img" aria-label="Photo of framed ads on a restroom wall"></div>
      <p>13" x 17" frames are strategically placed inside high traffic restrooms.</p>
      <a class="more" href="#">Find Out More »</a>
    </article>
    <article class="abs product p2">
      <h2>TallPlates</h2>
      <div class="product-photo" role="img" aria-label="Photo of backlit signs in a campus common area"></div>
      <p>48" x 72" backlit signs that are placed in high traffic common areas in cafeterias, student pubs and student centres, on College and Uni-versity campuses.</p>
      <a class="more" href="#">Find Out More »</a>
    </article>
    <article class="abs product p3">
      <h2>GrandFlags</h2>
      <div class="product-photo" role="img" aria-label="Photo of a stadium scoreboard and a wrapped ice resurfacer"></div>
      <p>These are large banners placed in high traffic common areas including on Glidewax Wraps, Wall Boards, Scoreboard Signage and Video Screens.</p>
      <a class="more" href="#">Find Out More »</a>
    </article>
  </section>

  <footer>
    <div class="abs footer-rule"></div>
    <div class="abs footer-info"><strong>Bravewell Display Group</strong><br>Copyright © 2012 Bravewell Display Group.&nbsp; All Rights Reserved.</div>
    <div class="abs footer-nav">
      <a href="#">Home</a><span>|</span><a href="#">Products</a><span>|</span><a href="#">Networks</a><span>|</span><a href="#">Effectiveness</a><span>|</span><a href="#">Campaigns</a><span>|</span><a href="#">Become a partner</a><span>|</span><a href="#">Contact Us</a>
    </div>
  </footer>
</div>
</body>
</html>
```